Flyer-Design für Musikverein - Jugendkapelle
Zielgruppe
Musikverein Hallbrunn
Unsere Zielgruppe sind Kinder und Jugendliche, die ein Instrument erlernen wollen.
Der Einstieg der jüngsten geht in einem Alter ab ca. 8 Jahren los. Die meisten neuen Musiker steigen zwischen 10 - 14 Jahren ein.
Der Flyer soll aber auch geeignet sein um an Grund- und weiterführenden Schulen ausgelegt werden zu können um Musiker für die Jugendkapelle zu gewinnen. Dementsprechend frisch und interessant soll der Flyer gestaltet sein.
Aufgabenstellung
Es soll ansprechend sein für Jugendliche, frisch, fröhlich und soll das Interesse der jugendlichen mit dem Design wecken.
Es soll die Jugendlichkeit, die Blasmusik und das Vereinsleben miteinander verbinden, sowie die Vorteile und der Spaß an der Musik (Instrument erlernen, Spaß am Musizieren, neue Freunde und Kameradschaft und auch Freizeitaktivitäten) miteinander darstellen.

```html
<!DOCTYPE html>
<html lang="de">
<head>
<meta charset="utf-8">
<title>Jugendkapelle Klangfunke – Musikverein Hallbrunn</title>
<link href="https://fonts.googleapis.com/css2?family=Work+Sans:wght@400;700;800&family=Caveat+Brush&display=swap" rel="stylesheet">
<style>
  :root {
    --leaf: #8cb46f;
    --leaf-light: #a3c38c;
    --text-white: #ffffff;
    --text-pale: #cfe1b4;
    --accent-red: #e8533d;
    --icon-pale: #e6eedc;
  }
  html, body {
    margin: 0;
    padding: 0;
    width: 1200px;
    height: 2572px;
    overflow: hidden;
  }
  body {
    background: var(--leaf);
    font-family: "Work Sans", Arial, sans-serif;
    color: var(--text-white);
    position: relative;
  }
  .paper-patch {
    position: absolute;
    left: 0;
    top: 1560px;
    width: 1200px;
    height: 900px;
  }
  .block { position: absolute; left: 110px; margin: 0; white-space: nowrap; }
  .intro {
    top: 162px;
    font-size: 38px;
    line-height: 52px;
    letter-spacing: 2px;
  }
  .intro strong { font-weight: 700; letter-spacing: 1.2px; }
  .intro p { margin: 0 0 52px; }
  .question {
    top: 708px;
    font-size: 46px;
    line-height: 61px;
    font-weight: 800;
    letter-spacing: 0.6px;
  }
  .invite {
    top: 1008px;
    font-size: 51px;
    line-height: 64px;
    font-weight: 800;
    color: var(--text-pale);
    letter-spacing: 0.4px;
  }
  .band-name {
    display: inline-block;
    background: var(--accent-red);
    color: var(--text-white);
    padding: 0 12px 0 10px;
    margin-left: 4px;
    transform: rotate(-1deg);
    line-height: 70px;
  }
  .instrument-icon {
    position: absolute;
    left: 568px;
    top: 1252px;
    width: 100px;
    height: 150px;
  }
  .info-heading {
    position: absolute;
    left: 108px;
    top: 1500px;
    margin: 0;
    font-family: "Caveat Brush", cursive;
    font-weight: 400;
    font-size: 106px;
    line-height: 110px;
    letter-spacing: 0;
    white-space: nowrap;
  }
  .web {
    top: 1648px;
    font-size: 38px;
    line-height: 52px;
    letter-spacing: 1.6px;
  }
  .web strong { font-weight: 800; letter-spacing: 0.5px; }
  .contact-lead {
    top: 1872px;
    font-size: 38px;
    line-height: 52px;
    letter-spacing: 1.6px;
  }
  .board {
    top: 2030px;
    font-size: 38px;
    line-height: 57px;
    letter-spacing: 1.6px;
  }
  .board h3 {
    margin: 0 0 12px;
    font-size: 40px;
    line-height: 52px;
    font-weight: 800;
    letter-spacing: 0.6px;
  }
  .board address { font-style: normal; }
  .board .reach { margin-top: 30px; }
  .welcome-tag {
    position: absolute;
    left: 636px;
    top: 1960px;
    width: 462px;
    padding: 16px 0 26px;
    background: var(--accent-red);
    transform: rotate(-5deg);
    font-family: "Caveat Brush", cursive;
    font-size: 82px;
    line-height: 72px;
    text-align: center;
    color: var(--text-white);
    white-space: nowrap;
  }
</style>
</head>
<body>

<svg class="paper-patch" viewBox="0 0 1200 900" aria-hidden="true">
  <path fill="var(--leaf-light)" d="M105 30 L160 20 L210 5 L230 25 L420 20 L640 50 L900 95 L1120 125 L1200 140 L1200 865 L1120 850 L900 810 L700 780 L540 730 L460 660 L380 600 L300 520 L220 420 L140 300 L95 200 L80 120 Z"/>
</svg>

<section class="block intro">
  <p>In unserer Jugendkapelle haben die <strong>Kinder</strong><br><strong>und Jugendlichen</strong> die Möglichkeit, nach <strong>1 bis</strong><br><strong>2-jähriger Ausbildung</strong> in der Gruppe zu spie-<br>len und zu üben.</p>
  <p>Danach geht es an das Musizieren im <strong>großen</strong><br><strong>Orchester.</strong> Letztendlich entscheiden die Diri-<br>genten und Ausbilder über den Eintritt in die<br>jeweiligen Orchester.</p>
</section>

<p class="block question">Oder du kannst schon ein Instrument<br>spielen und willst mit anderen gemein-<br>sam musizieren?</p>

<p class="block invite">Dann komm doch in die<br>Jugendkapelle<span class="band-name">„KLANGFUNKE“</span></p>

<div class="instrument-icon" role="img" aria-label="Kleines Symbol eines Blechblasinstruments (Tenorhorn)">
  <svg viewBox="0 0 100 150" width="100" height="150">
    <ellipse cx="52" cy="100" rx="36" ry="45" fill="var(--icon-pale)"/>
  </svg>
</div>

<h2 class="info-heading">Nähere Informationen:</h2>

<p class="block web">auf unserer Homepage unter:<br><strong>www.hallbrunn-blasmusik.de</strong></p>

<p class="block contact-lead">Oder kontaktiert<br>uns direkt:</p>

<section class="block board">
  <h3>Jugendvorstand:</h3>
  <address>
    Lena Albrecht<br>
    Lindenstr.<br>
    72999 Hallbrunn
    <div class="reach">Tel.: 0176 5 55 01 23<br>E-Mail: lena.albrecht@postfach-hallbrunn.de</div>
  </address>
</section>

<div class="welcome-tag">Wir freuen uns<br>auf Euch!</div>

</body>
</html>
```